GLOW RIDGE 21 DAY Challange

looking to make a poster that needs to be 36" wide x24"tall design graphic . Check out the added file as it is a rough draft of the material I would like it to say.

Phone number 555-302-4418 www.rgchiropractic..com

Adults aged 25-45 high income adults needing to make changes in dies and lose weight

```html
<!DOCTYPE html>
<html lang="en">
<head>
<meta charset="utf-8">
<title>GLOW RIDGE 21 Day Challenge Poster</title>
<link rel="stylesheet" href="https://fonts.googleapis.com/css2?family=Oswald:wght@600;700&family=Arimo:wght@400&display=swap">
<style>
  :root {
    --page: #f4f4f4;
    --cream: #fffccc;
    --green: #009a3e;
    --rust: #cc3300;
    --white: #ffffff;
    --ink: #111111;
    --produce-top: #b8ec8a;
    --produce-mid: #f6b48f;
    --produce-low: #ffd98a;
    --produce-end: #8fdca0;
  }
  * { margin: 0; padding: 0; box-sizing: border-box; }
  html, body {
    width: 1200px; height: 1000px; overflow: hidden;
    background: var(--page);
  }
  .poster {
    position: absolute; left: 53px; top: 154px;
    width: 1056px; height: 700px;
    background: var(--cream);
    overflow: hidden;
  }

  /* Title block */
  .title-block {
    position: absolute; left: 0; top: 0;
    width: 471px; height: 301px;
    background: var(--green);
    color: var(--white);
    font-family: "Oswald", "Arial Narrow", sans-serif;
    font-weight: 700;
    text-transform: uppercase;
  }
  .title-block span { position: absolute; left: 34px; white-space: nowrap; line-height: 1; }
  .title-name  { top: 2px;   font-size: 78px;  letter-spacing: -0.5px; }
  .title-days  { top: 78px;  font-size: 134px; letter-spacing: 0; }
  .title-word  { top: 196px; font-size: 80px;  letter-spacing: 1px; }

  /* Acrostic steps */
  .steps {
    position: absolute; left: 34px; top: 310px;
    list-style: none;
    font-family: "Arimo", Arial, sans-serif;
    font-size: 28px;
    color: var(--ink);
  }
  .steps li { height: 46px; display: flex; align-items: center; white-space: nowrap; }
  .step-letter {
    width: 43px;
    font-family: "Oswald", "Arial Narrow", sans-serif;
    font-weight: 700;
    font-size: 36px;
    color: var(--rust);
  }

  /* Produce illustration area */
  .produce-art {
    position: absolute; left: 482px; top: 30px;
    width: 248px; height: 520px;
  }

  /* Questions */
  .questions {
    position: absolute; left: 747px; top: 46px;
    list-style: none;
    font-family: "Arimo", Arial, sans-serif;
    font-size: 35px;
    line-height: 37px;
    color: var(--ink);
  }
  .questions li { margin-bottom: 15px; padding-left: 12px; text-indent: -12px; white-space: nowrap; }

  /* Call to action */
  .cta {
    position: absolute; left: 702px; top: 463px;
    width: 354px; height: 111px;
    background: var(--green);
    color: var(--white);
    font-family: "Oswald", "Arial Narrow", sans-serif;
    font-weight: 700;
    font-size: 54px;
    line-height: 52px;
    text-align: center;
    padding-top: 4px;
  }

  /* Contact band */
  .footer-band {
    position: absolute; left: 0; top: 595px;
    width: 1056px; height: 105px;
    background: var(--rust);
    color: var(--white);
    font-family: "Oswald", "Arial Narrow", sans-serif;
    font-weight: 600;
    font-size: 40px;
    display: flex; align-items: center; justify-content: center;
    gap: 80px;
  }
</style>
</head>
<body>
  <main class="poster">
    <header class="title-block">
      <span class="title-name">Glow Ridge</span>
      <span class="title-days">21 Day</span>
      <span class="title-word">Challenge</span>
    </header>

    <ul class="steps">
      <li><span class="step-letter">G</span>-Get Detox Supplements</li>
      <li><span class="step-letter">L</span>-Load Up on Omega 3</li>
      <li><span class="step-letter">O</span>-Opt for Vitamin D</li>
      <li><span class="step-letter">W</span>-Whole Fruits &amp; Veggies</li>
      <li><span class="step-letter">R</span>-Ridge Homemade Probiotic</li>
      <li><span class="step-letter">G</span>-Gentle Chiropractic Care</li>
    </ul>

    <svg class="produce-art" viewBox="0 0 248 520" role="img" aria-label="Illustration of fresh produce: green pepper, tomato, carrot, garlic, orange, mushrooms and a green apple">
      <defs>
        <linearGradient id="produceTones" x1="0" y1="0" x2="0" y2="1">
          <stop offset="0" stop-color="var(--produce-top)"/>
          <stop offset="0.35" stop-color="var(--produce-mid)"/>
          <stop offset="0.6" stop-color="var(--produce-low)"/>
          <stop offset="1" stop-color="var(--produce-end)"/>
        </linearGradient>
      </defs>
      <rect width="248" height="520" rx="24" fill="url(#produceTones)" opacity="0.55"/>
    </svg>

    <ul class="questions">
      <li>-Do you have<br>allergies?</li>
      <li>-Need to loose<br>weight?</li>
      <li>-Feel tired?</li>
      <li>-Have neck<br>or back pain?</li>
      <li>-Contain water,<br>weight?</li>
    </ul>

    <div class="cta">CALL TODAY<br>FOR DETAILS</div>

    <footer class="footer-band">
      <span class="contact-phone">555-302-4418</span>
      <span class="contact-web">www.rgchiropractic..com</span>
    </footer>
  </main>
</body>
</html>
```